creation of business cards for Velmora Sàrl

Velmora S% 26 # 224; rl is a soci% 26 # 233; t% 26 # 233; consultancy that accompanies companies in the development of their business on the market% 26 # 233; Switzerland by providing strategic contacts or market information; and by providing administrative or logistical support. Our consulting skills focus on sectors% 26 # 224; high value added% 26 # 233; e, such as trade in food goods% 26 # 39amp; drinks, fashion% 26amp; lifestyle, products and services for% 26 # 233; s in high-tech industries (pharmaceutical, chemical, m% 26 # 233; pricy 26% 23 #; cision) or sustainable solutions (% 26 # 233; energies renewable, mat% 26 # 233; recyclable materials). As part of the launch of our activity% 26 # 233;, we need% 26 # 39;% 26 # 233; to establish business cards to d% 26 # 233; work our new customers (Swiss or international).

Target Market(s)

Companies wishing to develop their activity% 26 # 233; s in Switzerland or% 26 # 224; l% 26 # 39;% 26 # 233; abroad (mainly in Europe).

Contact Information for Business Card

Prénom NOM
Velmora Sàrl
Bureau de Lavertin
Rue des Tilleuls 14, 2000 Neuchâtel
Tél. : 032 718 46 39
info@velmora-conseil.ch
www.velmora-conseil.ch

Font styles to use
Serif
Sans Serif

Colors

Designer to choose colors to be used in the design.

Requirements
Must have
• The logo The name of the company% 26 # 233; t% 26 # 233; (Velmora S% 26 # 224; rl) One field for the mailing address One field for the number% 26 # 233; ro de t% 26 # 233; l% 26 # 233; phone One field for the % 26 # 39; email address and website

```html
<!DOCTYPE html>
<html lang="fr">
<head>
<meta charset="UTF-8">
<title>Velmora Sàrl – cartes de visite</title>
<link href="https://fonts.googleapis.com/css2?family=Lato:wght@300;400;900&display=swap" rel="stylesheet">
<style>
  :root{
    --navy:#04405c;
    --mist:#a3b9c7;
    --paper:#ffffff;
    --ink-grey:#6d7378;
    --backdrop:#e4e7ea;
  }
  *{margin:0;padding:0;box-sizing:border-box}
  html,body{width:1200px;height:900px;overflow:hidden;background:var(--backdrop);font-family:'Lato',sans-serif}
  .stage{position:relative;width:1200px;height:900px}
  .card{position:absolute;left:280px;width:640px;height:366px;border-radius:22px;overflow:hidden;box-shadow:0 6px 18px rgba(0,0,0,.18)}
  .card-front{top:56px;background:var(--navy);display:flex;align-items:center;justify-content:center;gap:30px}
  .front-mark{width:62px;height:52px;border-radius:14px;background:var(--paper)}
  .front-name{color:var(--paper);font-weight:300;font-size:64px;letter-spacing:6px}
  .card-back{top:478px;background:var(--paper)}
  .back-wave{position:absolute;inset:0;width:100%;height:100%}
  .back-mark{position:absolute;left:118px;top:96px;width:176px;height:132px;border-radius:40px;background:var(--navy);display:flex;align-items:center;justify-content:center}
  .back-mark-name{color:var(--paper);font-weight:900;font-size:28px}
  .company{position:absolute;right:46px;top:36px;text-align:right}
  .company-name{color:var(--navy);font-weight:900;font-size:32px;line-height:1.1}
  .company-office{color:var(--ink-grey);font-weight:400;font-size:18px;margin-top:2px}
  .contact{position:absolute;right:22px;top:188px;color:var(--paper);font-size:14.5px;line-height:1.35;text-align:right;font-style:normal}
  .contact-address{margin-bottom:10px;margin-right:28px}
  .contact-line{display:flex;align-items:center;justify-content:flex-end;gap:10px}
  .contact-line svg{width:18px;height:18px;flex:none}
</style>
</head>
<body>
<main class="stage">
  <section class="card card-front" aria-label="Recto">
    <span class="front-mark"></span>
    <span class="front-name">VELMORA</span>
  </section>

  <section class="card card-back" aria-label="Verso">
    <svg class="back-wave" viewBox="0 0 640 366" preserveAspectRatio="none" aria-hidden="true">
      <path d="M0 322 C180 322 300 300 400 200 C470 130 540 112 640 104 V366 H0 Z" fill="var(--navy)"/>
      <path d="M0 290 C170 290 290 270 385 178 C450 118 510 96 585 86 C520 100 462 126 398 190 C300 286 175 302 0 302 Z" fill="var(--mist)"/>
    </svg>

    <div class="back-mark"><span class="back-mark-name">Velmora</span></div>

    <div class="company">
      <div class="company-name">Velmora Sàrl</div>
      <div class="company-office">Bureau de Lavertin</div>
    </div>

    <address class="contact">
      <div class="contact-address">Rue des Tilleuls 14,<br>2000 Neuchâtel</div>
      <div class="contact-line">032 718 46 39
        <svg viewBox="0 0 20 20"><path d="M5 2l3 3-2 2c1 3 3 5 6 6l2-2 3 3-2 3C8 17 3 12 2 4z" fill="var(--paper)"/></svg>
      </div>
      <div class="contact-line">info@velmora-conseil.ch
        <svg viewBox="0 0 20 20"><rect x="2" y="4" width="16" height="12" fill="none" stroke="var(--paper)" stroke-width="1.6"/><path d="M2 4l8 7 8-7" fill="none" stroke="var(--paper)" stroke-width="1.6"/></svg>
      </div>
      <div class="contact-line">www.velmora-conseil.ch
        <svg viewBox="0 0 20 20"><circle cx="10" cy="10" r="8" fill="none" stroke="var(--paper)" stroke-width="1.5"/><path d="M2 10h16M10 2v16M10 2c-4 4-4 12 0 16M10 2c4 4 4 12 0 16" fill="none" stroke="var(--paper)" stroke-width="1.2"/></svg>
      </div>
    </address>
  </section>
</main>
</body>
</html>
```